Drug safety monitoring company requires a new corporate website

We are an outsourcing partner to large and small companies within the pharmaceutical industry. Our current website www.quorvanta.co.uk has not been updated in a long time. We want a new web site that is responsive and modern but with a clearly corporate and professional feel. We want a design based on a 12 column grid system (mobile and desktop version). We want to use a new, modern font (not the standard web fonts) - we will purchase as required. Content can be used as is from the current website. Red and white are the corporate colours, so a palate should be developed to match. We do not need as much red as is in the current website. New icons (preferably in svg format) would be great. We can also purchase new images from Framly (or other) as required. We would prefer submissions in Sketch if possible.

Target Market(s)

Pharmaceutical companies

Number of Pages Required

1 page

Font styles to use
Sans Serif

Colors
ec1f27
ffffff

Requirements
Must have
• Design based on 12 column grid system.
Responsive design (i.e. require a mobile and desktop version).
How should the menu look between desktop and mobile?
A coherent colour palete.
Content to come from the existing website: www.quorvanta.co.uk
How should links be styled?
How should headings, sub-headings, paragraphs be styled?
Nice to have
• Custom developed icons (these are along the bottom of the page on the existing website: Medical Information; Pharmacovigilance; Literature Monitoring; Training).
New imagery (the images on the current website are dated).
Submission ideally as Sketch files (but we are okay with photoshop too).
A new, modern, non-standard font.
Not so much red in the design.
If we had buttons on the website, how should they be styled?
If we had a form on the website, how should the fields be styled?

```html
<!DOCTYPE html>
<html lang="en">
<head>
<meta charset="UTF-8">
<title>Menu</title>
<link rel="stylesheet" href="https://fonts.googleapis.com/css2?family=Kanit:wght@400;500&display=swap">
<style>
  :root {
    --brand-red: #ec1f27;
    --paper: #ffffff;
    --muted: #c9cbd1;
    --ink: #272a36;
  }
  html, body {
    margin: 0;
    padding: 0;
    width: 1200px;
    height: 2700px;
    overflow: hidden;
    background: var(--paper);
    font-family: "Kanit", sans-serif;
  }
  .mobile-menu {
    position: relative;
    width: 1200px;
    height: 2700px;
    background: var(--paper);
  }
  .menu-close {
    position: absolute;
    left: 1060px;
    top: 164px;
    width: 54px;
    height: 54px;
  }
  .menu-list {
    list-style: none;
    margin: 0;
    padding: 0;
  }
  .menu-item {
    position: absolute;
    left: 76px;
    height: 104px;
    line-height: 104px;
    font-size: 74px;
    font-weight: 500;
    color: var(--muted);
    white-space: nowrap;
  }
  .menu-item.is-active {
    color: var(--brand-red);
    display: flex;
    align-items: center;
  }
  .active-dash {
    display: inline-block;
    width: 54px;
    height: 7px;
    background: var(--brand-red);
    margin-right: 24px;
  }
  .submenu-item {
    position: absolute;
    left: 150px;
    height: 84px;
    line-height: 84px;
    font-size: 58px;
    font-weight: 400;
    color: var(--ink);
    white-space: nowrap;
  }
</style>
</head>
<body>
  <nav class="mobile-menu" aria-label="Main menu">
    <svg class="menu-close" viewBox="0 0 52 52" aria-label="Close menu" role="img">
      <line x1="4" y1="4" x2="48" y2="48" stroke="var(--ink)" stroke-width="6" stroke-linecap="round"/>
      <line x1="48" y1="4" x2="4" y2="48" stroke="var(--ink)" stroke-width="6" stroke-linecap="round"/>
    </svg>
    <ul class="menu-list">
      <li class="menu-item" style="top:355px">Home</li>
      <li class="menu-item" style="top:558px">About Us</li>
      <li class="menu-item" style="top:761px">QPPV</li>
      <li class="menu-item is-active" style="top:961px"><span class="active-dash"></span>Our Services</li>
      <li class="submenu-item" style="top:1135px">Safetylink</li>
      <li class="submenu-item" style="top:1295px">Pharmacovigilance</li>
      <li class="submenu-item" style="top:1452px">Medical Information</li>
      <li class="submenu-item" style="top:1612px">Literature Monitoring</li>
      <li class="submenu-item" style="top:1768px">Medical Devices</li>
      <li class="submenu-item" style="top:1925px">Training</li>
      <li class="menu-item" style="top:2110px">Contact Us</li>
      <li class="menu-item" style="top:2310px">Client</li>
    </ul>
  </nav>
</body>
</html>
```